rosie's empada

We are a family business based in sydney introducing a common brazilian street food into sydney cafes and restaurants.
what we provide are pastels which is a thinly crust pie with assorted fillings
we mainly focus on supplying cafes and restaurants but we do sell privately.
We have had a few cafes ask to stock our cards due to customer request. except we don't have any!! hence why we need you. : )
I have attached an image of our pastels which is just to give you an idea of what they look like.
Updates
I have just seen all the designs and am impressed by some of your work. I will have to sit with my parter later today and will hopefully have some more constructive feedback and a decision soon.
Hello designers,
Hello designers,
Target Market(s)
cafe's and restaurants
Industry/Entity Type
Business
Contact Information for Business Card
Rosie's empada
joaquim 0428716904
rosiesempada@fernmail.com

```html
<!DOCTYPE html>
<html lang="en">
<head>
<meta charset="utf-8">
<title>Rosie's empada – business card</title>
<link rel="stylesheet" href="https://fonts.googleapis.com/css2?family=Coustard:wght@900&display=swap">
<style>
  :root {
    --card-white: #ffffff;
    --brand-red: #d0262a;
    --swoosh-orange: #ec8a2c;
    --contact-orange: #f2a023;
    --text-white: #ffffff;
  }
  html, body {
    margin: 0;
    padding: 0;
    overflow: hidden;
    background: var(--card-white);
  }
  .card {
    position: relative;
    width: 1200px;
    height: 741px;
    overflow: hidden;
    background: var(--card-white);
    font-family: "Coustard", Georgia, serif;
    font-weight: 900;
  }
  .swoosh {
    position: absolute;
    inset: 0;
    width: 1200px;
    height: 741px;
  }
  .brand {
    position: absolute;
    left: 62px;
    top: 150px;
    width: 660px;
    height: 200px;
    display: flex;
    align-items: center;
    gap: 28px;
  }
  .brand-mark {
    flex: 0 0 150px;
    width: 150px;
    height: 150px;
    border-radius: 50%;
    background: var(--swoosh-orange);
  }
  .brand-name {
    margin: 0;
    color: var(--brand-red);
    font-size: 66px;
    line-height: 1.05;
    font-weight: 900;
  }
  .contacts {
    position: absolute;
    right: 72px;
    top: 496px;
    margin: 0;
    text-align: right;
    font-style: normal;
    font-size: 42px;
    line-height: 58px;
  }
  .contacts p { margin: 0; }
  .contact-name { color: var(--text-white); }
  .contact-detail { color: var(--contact-orange); }
</style>
</head>
<body>
  <main class="card">
    <svg class="swoosh" viewBox="0 0 1110 685" preserveAspectRatio="none" aria-hidden="true">
      <path fill="var(--swoosh-orange)"
            d="M590 430 C 800 403 1000 298 1110 118 L1110 178 C 1040 298 900 376 720 418 Z"/>
      <path fill="var(--brand-red)"
            d="M0 685 L0 652 C 200 550 460 455 720 418 C 900 380 1045 298 1110 175 L1110 685 Z"/>
    </svg>

    <header class="brand">
      <span class="brand-mark" aria-hidden="true"></span>
      <h1 class="brand-name">Rosie's empada</h1>
    </header>

    <address class="contacts">
      <p><span class="contact-name">Joaquim</span> <span class="contact-detail">0428716904</span></p>
      <p><span class="contact-name">Rosie</span> <span class="contact-detail">0417203589</span></p>
      <p><span class="contact-detail">rosiesempada@fernmail.com</span></p>
    </address>
  </main>
</body>
</html>
```